Fresh pet feed direct from manufacturer to door step. Quality and Freshness un-surpassed in Industr

Need Business Card Design; leading into many other projects, for New Franchised Business Opportunity providing home delivery of fresh dog and cat feed (no emphasis needed for cat) direct from manufacturing facility. (no middle men or distributors) Food is Farm to Factory fresh. Our trademarked tagline is "Quality is our MAIN Ingredient ! "
Updates

Please take note of other contest for Facebook Cover and Profile Pic's

Target Market(s)

Dog and Cat owners

Industry/Entity Type

Pet

Contact Information for Business Card

Name, address, local phone, national 800 number, website, email address

Other font styles liked:
• follow that from logo

Requirements
Must have
• Our feed is made in Texas with ingredients sourced from local farms. We want to lean heavy on the Made in West Texas , ranch theme but that has a 'black label', 'vantrell', 'premium', 'high-end' look and feel
Nice to have
• maybe have an offer on card? 20% off with promo code "x" etc.. ?? just a thought...

```html
<!DOCTYPE html>
<html lang="en">
<head>
<meta charset="utf-8">
<title>Redmesa Feed Co. — Business Card</title>
<link rel="stylesheet" href="https://fonts.googleapis.com/css2?family=Roboto:wght@300;400&display=swap">
<style>
  :root {
    --backdrop: #e9e6e1;
    --card: #f7f7f6;
    --band: #231a26;
    --band-edge: #120d14;
    --gold: #e2cb2a;
    --ink: #1f1d21;
    --muted: #4a474c;
  }
  * { margin: 0; padding: 0; box-sizing: border-box; }
  html, body {
    width: 1200px; height: 858px; overflow: hidden;
    background: var(--backdrop);
    font-family: "Roboto", Arial, sans-serif;
  }
  .canvas {
    width: 1200px; height: 858px;
    display: flex; align-items: center; justify-content: center; gap: 40px;
  }
  .card {
    position: relative;
    width: 545px; height: 312px;
    background: var(--card);
    box-shadow: 0 8px 24px rgba(0,0,0,.18);
    overflow: hidden;
  }

  /* Front */
  .card--front { border-top: 6px solid var(--gold); }
  .front__band {
    position: absolute; left: 0; right: 0; bottom: 0; height: 64px;
    background: linear-gradient(var(--band), var(--band-edge));
  }
  .front__address {
    position: absolute; right: 60px; bottom: 22px;
    color: var(--gold); font-weight: 300; font-size: 17px; letter-spacing: .2px;
  }
  .brand {
    display: flex; align-items: center; gap: 10px;
    color: var(--band); font-weight: 400;
  }
  .brand__dot { width: 14px; height: 14px; border-radius: 50%; background: var(--gold); flex: none; }
  .brand__name { font-size: 26px; line-height: 1; }
  .front__brand { position: absolute; right: 60px; top: 52px; }
  .front__name {
    position: absolute; left: 44px; top: 116px;
    font-weight: 300; font-size: 22px; color: var(--ink);
  }
  .contacts {
    position: absolute; left: 150px; top: 154px;
    list-style: none; font-weight: 300; font-size: 14px; color: var(--muted);
  }
  .contacts li { display: flex; align-items: center; gap: 10px; height: 21px; }
  .contacts svg { width: 11px; height: 11px; fill: var(--gold); flex: none; }

  /* Back */
  .card--back { border-bottom: 6px solid var(--gold); }
  .back__band {
    position: absolute; left: 0; right: 0; top: 0; height: 34px;
    background: linear-gradient(var(--band-edge), #2a2a2a);
  }
  .back__rule {
    position: absolute; left: 0; right: 0; top: 40px; height: 3px; background: var(--gold);
  }
  .back__brand {
    position: absolute; left: 0; right: 0; top: 150px;
    justify-content: center;
  }
  .back__brand .brand__name { font-size: 30px; }
</style>
</head>
<body>
<main class="canvas">
  <article class="card card--front">
    <div class="brand front__brand">
      <span class="brand__dot"></span>
      <span class="brand__name">Redmesa Feed Co.</span>
    </div>
    <p class="front__name">Your Name</p>
    <ul class="contacts">
      <li><svg viewBox="0 0 12 12"><path d="M2 1l2.5 0 1 3-1.5 1c.7 1.4 1.6 2.3 3 3l1-1.5 3 1V11.5C5.5 11.5.5 6.5.5 1z"/></svg>000 - 0000 000</li>
      <li><svg viewBox="0 0 12 12"><path d="M2 1l2.5 0 1 3-1.5 1c.7 1.4 1.6 2.3 3 3l1-1.5 3 1V11.5C5.5 11.5.5 6.5.5 1z"/></svg>000 - 0000 000</li>
      <li><svg viewBox="0 0 12 12"><circle cx="6" cy="6" r="5.5"/></svg>www.redmesafeed.com</li>
      <li><svg viewBox="0 0 12 12"><path d="M.5 2.5h11v7h-11zM1 3l5 3.5L11 3v1L6 7.5 1 4z"/></svg>name@redmesafeed.com</li>
    </ul>
    <div class="front__band"></div>
    <p class="front__address">000 west, 1st street UA 00000</p>
  </article>

  <article class="card card--back">
    <div class="back__band"></div>
    <div class="back__rule"></div>
    <div class="brand back__brand">
      <span class="brand__dot"></span>
      <span class="brand__name">Redmesa Feed Co.</span>
    </div>
  </article>
</main>
</body>
</html>
```